Consulting Engineering Firm WordPress Design

We need:
1. A WordPress design.
2. Company is based in Sydney, Australia.
3. Company name: K7R Consulting Engineers.
The company provide professional engineering consultancy services to building owners, operators, developers and designers.
4. Overall purpose or objective of the website: The website must reflect high professionalism. It will provide information to our clients on who we are, what we do, how we do, our experience, projects we have done in the past and contact information.
5. Company logo is in the uploaded files.
6. Webpage:
6.1. Standard Web pages. Not for e-commercial.
6.2. Use WordPress. Website will be hosted on Hostvane WordPress hosting.
7. Coding required.
8. The winning designer (Winner) shall assist to host the wordpress design on Hostvane WordPress hosting services. Winner will transfer the files and configure to make sure all pages, links, posts and blogs works as intended.
8. We would like the site to have the same theme as the company brochure which is uploaded here.
9. The SSL certificate must be configured in the coded WordPress.
10. Pages:
i. Home - will have images updating every 4 s. Refer to company brochure for the images I am after. Use similar or better high quality images.
ii. About Us
iii. Services - This will have sub pages.
iv. Markets- This will have sub pages.
v. Projects- This will have sub pages.
vi. Contact - This will have company contact details. Also, it will request first name, last name, phone number, email address, comments and submit button.
11. I want a clean, minimalist websites that has a more professional tone. Please do not use too much unnecessary graphical elements and avoid loud vibrant colours.
12. Use images related to technology, buildings, smart city, smart buildings, energy savings, control system, energy dash boards, etc.
Target Market(s)
Building services engineering consultants, builders, building owners, building managers.

```html
<!DOCTYPE html>
<html lang="en">
<head>
<meta charset="utf-8">
<title>K7R Consulting Engineers</title>
<link href="https://fonts.googleapis.com/css2?family=Montserrat:wght@500;600;700;800&family=Arimo:wght@400;700&display=swap" rel="stylesheet">
<style>
:root{
  --teal:#13a88e;
  --blue:#0b3f9e;
  --blue-deep:#0a3a93;
  --ink:#1d1d1f;
  --text:#5c5c5c;
  --sky:#e8f5fc;
  --line:#c9c9c9;
  --field:#f2f2f2;
  --white:#ffffff;
}
*{box-sizing:border-box;margin:0;padding:0}
html,body{width:1200px;height:4444px;overflow:hidden}
body{position:relative;font-family:"Arimo",Arial,sans-serif;color:var(--text);background:var(--white)}
.abs{position:absolute}
h1,h2,h3,h4{font-family:"Montserrat",Arial,sans-serif;color:var(--ink)}
.btn{position:absolute;display:flex;align-items:center;justify-content:center;background:var(--teal);color:var(--white);font-family:"Montserrat",Arial,sans-serif;font-weight:700;font-size:14px;border-radius:24px;letter-spacing:.3px}
p.body{font-size:13.4px;line-height:22.5px;text-align:justify}

/* header */
.site-header{position:absolute;top:0;left:0;width:1200px;height:100px;background:var(--white)}
.brand{position:absolute;left:110px;top:22px;display:flex;align-items:center;gap:10px}
.brand-dot{width:52px;height:52px;border-radius:50%;background:var(--blue)}
.brand-name{font-family:"Montserrat",Arial,sans-serif;font-weight:700;font-size:17px;color:var(--blue);line-height:20px;width:150px}
.nav{position:absolute;top:40px;left:408px;display:flex;gap:28px;font-family:"Arimo",Arial,sans-serif;font-weight:700;font-size:14px;color:var(--ink)}
.nav .active{color:var(--teal)}
.nav-marker{position:absolute;left:418px;top:0;width:0;height:0;border-left:12px solid transparent;border-right:12px solid transparent;border-top:22px solid var(--blue)}
.login{position:absolute;left:1018px;top:40px;font-weight:700;font-size:14px;color:var(--teal);text-decoration:underline;display:flex;align-items:center;gap:6px}

/* hero */
.hero{position:absolute;top:100px;left:0;width:1200px;height:573px;background:linear-gradient(160deg,#c9c6c0 0%,#8f9aa3 35%,#5a6d78 65%,#3d4a46 100%)}
.hero-title{position:absolute;left:108px;top:200px;font-size:51px;font-weight:800;color:var(--white);line-height:54px;text-shadow:0 2px 6px rgba(0,0,0,.35)}
.dots{position:absolute;left:1139px;top:238px;display:flex;flex-direction:column;gap:9px}
.dots span{width:11px;height:11px;border-radius:50%;background:var(--white)}
.dots span.on{background:var(--teal)}

/* services */
.services{position:absolute;top:673px;left:0;width:1200px;height:711px;background:var(--sky)}
.section-title{position:absolute;left:0;width:1200px;text-align:center;font-size:34px;font-weight:700}
.card{position:absolute;width:483px;height:210px;background:var(--white);border-bottom:5px solid var(--blue)}
.card.left{border-left:5px solid var(--blue)}
.card.right{border-right:5px solid var(--blue)}
.card h3{position:absolute;left:205px;top:30px;font-size:21px;font-weight:600}
.card p{position:absolute;left:206px;top:70px;width:245px;font-size:13.2px;line-height:22.4px}
.card-icon{position:absolute;left:40px;top:36px;width:130px;height:130px;border-radius:50%;background:linear-gradient(135deg,#e3ecf8,#c4d4ec)}
.badge{position:absolute;left:534px;top:1328px;width:132px;height:132px;border-radius:50%;background:linear-gradient(135deg,var(--teal),var(--blue))}

/* about */
.about-art{position:absolute;left:181px;top:1558px;width:328px;height:353px;border-radius:8px;background:linear-gradient(160deg,#d9e3ef 0%,#8d9cab 50%,#4a5c70 100%)}
.about h2,.markets h2{font-size:33px;font-weight:700}
.about h3{font-size:25px;font-weight:700;color:var(--blue);margin-top:10px}

/* projects */
.projects{position:absolute;top:2470px;left:0;width:1200px;height:687px;background:linear-gradient(135deg,#0ea98d 0%,#0a7f9c 45%,#0b4aa0 100%)}
.projects .section-title{color:var(--white)}
.project{position:absolute;top:171px;width:311px}
.project .ph{height:219px;border-radius:22px 22px 0 0}
.project h4{color:var(--white);font-size:21px;font-weight:700;line-height:29px;margin-top:16px}
.project .rule{width:96px;height:2px;background:rgba(255,255,255,.7);margin:14px 0 12px}
.project p{color:var(--white);font-size:12.8px;line-height:22px}
.project .more{color:var(--white);font-weight:700;font-size:13px;text-decoration:underline;margin-top:12px;display:block}

/* contact */
.info{position:absolute;top:3370px;width:200px;text-align:center}
.info .ring{width:64px;height:64px;border:2px solid var(--blue);border-radius:50%;margin:0 auto;display:flex;align-items:center;justify-content:center}
.info h4{font-family:"Arimo",Arial,sans-serif;font-size:13px;color:var(--ink);margin-top:14px}
.info p{font-size:12.5px;line-height:20px;margin-top:4px}
.field{position:absolute;background:var(--field);border:1px solid var(--line);font-size:13px;color:#777;padding:18px 22px}

/* footer */
.footer{position:absolute;top:3980px;left:0;width:1200px;height:464px}
.footer-body{position:absolute;top:125px;left:0;width:1200px;height:339px;background:var(--blue-deep)}
.footer h4{position:absolute;color:var(--white);font-size:20px;font-weight:600}
.footer ul{position:absolute;list-style:none;color:var(--white);font-size:13px;line-height:22.5px}
.footer ul.links li::before{content:"›";color:var(--teal);margin-right:10px}
.fbrand{position:absolute;left:110px;top:178px;display:flex;align-items:center;gap:12px}
.fbrand .brand-dot{background:var(--white);width:70px;height:70px}
.fbrand .brand-name{color:var(--white);font-size:20px;line-height:24px;width:170px}
.social{position:absolute;left:110px;top:4277px;display:flex;gap:6px}
.social span{width:34px;height:34px;border-radius:50%;background:var(--white)}
.copyright{position:absolute;top:4396px;left:0;width:1200px;text-align:center;color:var(--white);font-size:12px}
</style>
</head>
<body>

<header class="site-header">
  <div class="brand"><span class="brand-dot"></span><span class="brand-name">K7R Consulting Engineers</span></div>
  <span class="nav-marker"></span>
  <nav class="nav"><span class="active">HOME</span><span>ABOUT US</span><span>SERVICES</span><span>MARKETS</span><span>PROJECTS</span><span>CONTACT</span></nav>
  <span class="login"><svg width="16" height="16" viewBox="0 0 16 16"><circle cx="8" cy="8" r="7" fill="none" stroke="currentColor" stroke-width="1.6"/><circle cx="8" cy="6.5" r="2.4" fill="currentColor"/><path d="M3.8 12.5c1-2 2.5-2.8 4.2-2.8s3.2.8 4.2 2.8" fill="currentColor"/></svg>LOGIN</span>
</header>

<section class="hero" role="img" aria-label="Aerial view of Sydney harbour bridge and city skyline at sunrise">
  <h1 class="hero-title">K7R CONSULTING<br>ENGINEERS</h1>
  <span class="btn" style="left:109px;top:331px;width:153px;height:43px">GET STARTED</span>
  <div class="dots"><span></span><span class="on"></span><span></span><span></span><span></span></div>
</section>

<section class="services">
  <h2 class="section-title" style="top:96px">CONSULTANCY SERVICES</h2>

  <div class="card left" style="left:103px;top:169px">
    <div class="card-icon" role="img" aria-label="Building owner icon"></div>
    <h3>BUILDING OWNERS</h3>
    <p>Lorem ipsum dolor sit amet, consectetu radipscing elit, sed do eiusmod tempor incididunt ut labore et dolore magna aliqua. Ut enim ad minim veniam, quis nostrud exercitation</p>
  </div>
  <div class="card right" style="left:604px;top:169px">
    <div class="card-icon" role="img" aria-label="Operator icon"></div>
    <h3>OPERATORS</h3>
    <p>Lorem ipsum dolor sit amet, consectetu radipscing elit, sed do eiusmod tempor incididunt ut labore et dolore magna aliqua. Ut enim ad minim veniam, quis nostrud exercitation</p>
  </div>
  <div class="card left" style="left:103px;top:397px">
    <div class="card-icon" role="img" aria-label="Developer icon"></div>
    <h3>DEVELOPERS</h3>
    <p>Lorem ipsum dolor sit amet, consectetu radipscing elit, sed do eiusmod tempor incididunt ut labore et dolore magna aliqua. Ut enim ad minim veniam, quis nostrud exercitation</p>
  </div>
  <div class="card right" style="left:604px;top:397px">
    <div class="card-icon" role="img" aria-label="Designer tools icon"></div>
    <h3>DESIGNERS</h3>
    <p>Lorem ipsum dolor sit amet, consectetu radipscing elit, sed do eiusmod tempor incididunt ut labore et dolore magna aliqua. Ut enim ad minim veniam, quis nostrud exercitation</p>
  </div>
</section>

<div class="badge" role="img" aria-label="Office building icon"></div>

<section class="about">
  <div class="about-art" role="img" aria-label="Tall glass office buildings seen from below"></div>
  <div class="abs" style="left:616px;top:1550px;width:470px">
    <h2>ABOUT US</h2>
    <h3>K7R CONSULTING ENGINEERS</h3>
    <p class="body" style="margin-top:12px">Lorem ipsum dolor sit amet, consectetur adipscing elit, sed do eiusmod tempor incididunt ut labore et dolore magna aliqua. Ut enim ad minim venia m, quis nostrud exercitation ullamco laboris nisi ut aliquip ex ea commodo consequat. Duis aute irure dolor in reprehenderit in voluptate velit esse cillum dolore eu fugiat nulla pariatur. Excepteur sint occaecat cupidatat non proident, sunt in culpa qui officia deserunt mollit anim id est laborum.Lorem ipsum dolor sit amet, consectetur adipscing elit, sed do eiusmod tempor incididunt ut labore et dolore magna aliqua. Ut enim ad minim venia m, quis nostrud exercitation ullamco laboris nisi ut</p>
  </div>
  <span class="btn" style="left:617px;top:1862px;width:152px;height:43px">LEARN MORE</span>
</section>

<section class="markets">
  <div class="abs" style="left:110px;top:2000px;width:470px">
    <h2>MARKETS</h2>
    <p class="body" style="margin-top:12px">Lorem ipsum dolor sit amet, consectetur adipscing elit, sed do eiusmod tempor incididunt ut labore et dolore magna aliqua. Ut enim ad minim venia m, quis nostrud exercitation ullamco laboris nisi ut aliquip ex ea commodo consequat. Duis aute irure dolor in reprehenderit in voluptate velit esse cillum dolore eu fugiat nulla pariatur. Excepteur sint occaecat cupidatat non proident, sunt in culpa qui officia deserunt mollit anim id est laborum.Lorem ipsum dolor sit amet, consectetur adipscing elit, sed do eiusmod tempor incididunt ut labore et dolore magna aliqua. Ut enim ad minim venia m, quis nostrud exercitation ullamco laboris nisi ut Lorem ipsum dolor sit amet, consectetur adipscing elit, sed do eiusmod tempor incididunt ut labore et dolore magna aliqua. Ut enim ad minim venia m, quis nostrud exercitation ullamco</p>
  </div>
  <span class="btn" style="left:112px;top:2321px;width:152px;height:44px">LEARN MORE</span>
  <div class="abs" role="img" aria-label="Aerial view of city towers and streets" style="left:621px;top:2011px;width:467px;height:356px;background:linear-gradient(150deg,#9fb4c4,#51677a 50%,#2b3a48)"></div>
</section>

<section class="projects">
  <h2 class="section-title" style="top:90px">RECENT PROJECTS</h2>
  <article class="project" style="left:110px">
    <div class="ph" role="img" aria-label="Engineers reviewing building plans on a desk" style="background:linear-gradient(160deg,#c9c4ba,#8a857c)"></div>
    <h4>Lorem ipsum dolor sit amet, consectetur adipiscing</h4><div class="rule"></div>
    <p>Lorem ipsum dolor sit amet, consectetur adipiscing elit, sed do eiusmod tempor incididunt ut labore et dolore magna aliqua.</p>
    <span class="more">Learn more ➔</span>
  </article>
  <article class="project" style="left:443px">
    <div class="ph" role="img" aria-label="Site team in high-visibility vests inside a warehouse" style="background:linear-gradient(160deg,#b8bcc0,#5d6a5c 60%,#c9cf5a)"></div>
    <h4>Lorem ipsum dolor sit amet, consectetur adipiscing</h4><div class="rule"></div>
    <p>Lorem ipsum dolor sit amet, consectetur adipiscing elit, sed do eiusmod tempor incididunt ut labore et dolore magna aliqua.</p>
    <span class="more">Learn more ➔</span>
  </article>
  <article class="project" style="left:778px">
    <div class="ph" role="img" aria-label="Engineers on a video call at a laptop" style="background:linear-gradient(160deg,#d8d4cc,#7c7870 55%,#3d3b38)"></div>
    <h4>Lorem ipsum dolor sit amet, consectetur adipiscing</h4><div class="rule"></div>
    <p>Lorem ipsum dolor sit amet, consectetur adipiscing elit, sed do eiusmod tempor incididunt ut labore et dolore magna aliqua.</p>
    <span class="more">Learn more ➔</span>
  </article>
</section>

<section class="contact">
  <h2 class="section-title" style="top:3250px">CONTACT US</h2>
  <p class="abs" style="top:3303px;left:0;width:1200px;text-align:center;font-size:13.5px">Lorem ipsum dolor sit amet, consectetur adipiscing elit, sed do eiusmod</p>

  <div class="info" style="left:267px">
    <div class="ring"><svg width="22" height="26" viewBox="0 0 22 26"><path d="M11 1a8 8 0 0 1 8 8c0 6-8 15-8 15S3 15 3 9a8 8 0 0 1 8-8z" fill="var(--teal)"/><circle cx="11" cy="9" r="3" fill="#fff"/></svg></div>
    <h4>ADDRESS :</h4><p>Lorem ipsum dolor sit amet,<br>consectetur adipisci</p>
  </div>
  <div class="info" style="left:507px">
    <div class="ring"><svg width="22" height="22" viewBox="0 0 24 24"><path d="M6.6 10.8a15 15 0 0 0 6.6 6.6l2.2-2.2a1 1 0 0 1 1-.25 11.4 11.4 0 0 0 3.6.57 1 1 0 0 1 1 1V20a1 1 0 0 1-1 1A17 17 0 0 1 3 4a1 1 0 0 1 1-1h3.5a1 1 0 0 1 1 1c0 1.25.2 2.45.57 3.570a1 1 0 0 1-.25 1z" fill="var(--teal)"/></svg></div>
    <h4>PHONE :</h4><p>+1 888 888 8888</p>
  </div>
  <div class="info" style="left:746px">
    <div class="ring"><svg width="24" height="18" viewBox="0 0 24 18"><rect x="1" y="1" width="22" height="16" rx="2" fill="var(--teal)"/><path d="M2 3l10 7 10-7" fill="none" stroke="#fff" stroke-width="2"/></svg></div>
    <h4>EMAIL :</h4><p>info@companyname.com</p>
  </div>

  <div class="field" style="left:238px;top:3533px;width:352px;height:59px">First name</div>
  <div class="field" style="left:607px;top:3533px;width:352px;height:59px">Last name</div>
  <div class="field" style="left:238px;top:3609px;width:352px;height:58px">Phone</div>
  <div class="field" style="left:607px;top:3609px;width:352px;height:58px">Email address</div>
  <div class="field" style="left:238px;top:3686px;width:721px;height:133px">Message</div>
  <span class="btn" style="left:521px;top:3843px;width:159px;height:49px">SUBMIT</span>
</section>

<footer class="footer">
  <svg class="abs" style="left:0;top:0" width="1200" height="130" viewBox="0 0 1200 130" preserveAspectRatio="none">
    <path d="M0 90 C300 10 800 -10 1200 60 L1200 130 L0 130z" fill="var(--teal)"/>
    <path d="M0 125 C300 40 800 20 1200 105 L1200 130 L0 130z" fill="var(--blue-deep)"/>
  </svg>
  <div class="footer-body"></div>
  <div class="fbrand"><span class="brand-dot"></span><span class="brand-name">K7R Consulting Engineers</span></div>
  <h4 style="left:386px;top:170px">Quick links</h4>
  <ul class="links" style="left:386px;top:212px"><li>Home</li><li>About us</li><li>Services</li><li>Clients</li><li>Contact us</li></ul>
  <h4 style="left:574px;top:170px">Contact us</h4>
  <ul style="left:574px;top:212px"><li style="padding-left:26px">123,Lorem ipsum dolor sit amet,</li><li style="padding-left:26px">consectetur adipisci</li><li style="margin-top:22px;padding-left:26px">+1 888 888 8888</li><li style="padding-left:26px">info@companyname.com</li></ul>
  <h4 style="left:857px;top:170px">Newsletter</h4>
  <div class="abs" style="left:858px;top:224px;width:230px;height:30px;border-bottom:1px solid rgba(255,255,255,.7);color:#fff;font-size:13px;padding-left:8px">Email address</div>
  <span class="btn" style="left:858px;top:272px;width:159px;height:49px">SUBMIT</span>
</footer>
<div class="social" aria-label="Social links"><span></span><span></span><span></span><span></span></div>
<p class="copyright">© Copyrights Company name 2021. All rights reserved | Privacy policy | Terms Condition</p>

</body>
</html>
```